Business Card Design Project

We need a business card design for a relatively new company called Lumen Stride. We design paddle (an outdoor winter sport primarily played in the midwest and east coast) and tennis bags for women and men. Lumen Stride is a lifestyle brand for the next generation country club goers. Our bags merge fashion with functionality and are making country club sports trendier and more fashionable.

I would like to include space for
Name: (will fill this in for employees)
Lumen Stride
Phone: (will do this)
Email:
www.lumenstride-example.net

Would also like to include Facebook and Twitter icons.
Please do not use pictures of the bags - this is just to give you an idea of what style bags we sell.

Target Market(s)

30 to 40 year old men and women - luxury market

Industry/Entity Type

Fashion

Requirements
Must have
• Would like the company logo included

```html
<!DOCTYPE html>
<html lang="en">
<head>
<meta charset="utf-8">
<title>Lumen Stride — Business Card</title>
<link rel="stylesheet" href="https://fonts.googleapis.com/css2?family=Questrial&family=Open+Sans:ital,wght@0,400;0,700;1,400&display=swap">
<style>
  :root {
    --brand-orange: #f05a24;
    --card-white: #ffffff;
    --page-bg: #ffffff;
    --ink-dark: #2b2b2b;
    --text-light: #ffffff;
    --shadow: rgba(0, 0, 0, 0.28);
  }
  * { box-sizing: border-box; margin: 0; padding: 0; }
  html, body {
    width: 1200px;
    height: 1200px;
    overflow: hidden;
    background: var(--page-bg);
  }
  .canvas {
    position: relative;
    width: 1200px;
    height: 1200px;
    background: var(--page-bg);
  }
  .card {
    position: absolute;
    width: 700px;
    height: 400px;
    box-shadow: 0 18px 40px var(--shadow);
  }

  /* Card back */
  .card-back {
    left: 110px;
    top: 170px;
    background: var(--card-white);
    display: flex;
    align-items: center;
    justify-content: center;
    gap: 22px;
  }
  .card-back .mark-dot {
    width: 96px;
    height: 96px;
    border-radius: 50%;
    background: var(--brand-orange);
  }
  .card-back .brand-name {
    font-family: "Questrial", sans-serif;
    font-size: 64px;
    color: var(--brand-orange);
    letter-spacing: 1px;
  }

  /* Card front */
  .card-front {
    left: 420px;
    top: 520px;
    background: var(--brand-orange);
    color: var(--text-light);
  }
  .card-front .brand-row {
    position: absolute;
    left: 34px;
    top: 38px;
    display: flex;
    align-items: center;
    gap: 16px;
  }
  .card-front .brand-row .mark-dot {
    width: 44px;
    height: 44px;
    border-radius: 50%;
    background: var(--text-light);
  }
  .card-front .brand-name {
    font-family: "Questrial", sans-serif;
    font-size: 58px;
    line-height: 1;
    color: var(--text-light);
  }
  .card-front .person {
    position: absolute;
    left: 34px;
    top: 160px;
    font-family: "Open Sans", sans-serif;
  }
  .card-front .person-name {
    font-weight: 700;
    font-size: 22px;
    letter-spacing: 0.5px;
  }
  .card-front .person-role {
    font-style: italic;
    font-size: 15px;
    margin-top: 2px;
  }
  .card-front .contact {
    position: absolute;
    left: 34px;
    bottom: 28px;
    display: flex;
    align-items: center;
    gap: 12px;
  }
  .card-front .contact .mark-dot {
    width: 26px;
    height: 26px;
    border-radius: 50%;
    background: var(--text-light);
  }
  .card-front .contact-lines {
    border-left: 2px solid var(--text-light);
    padding-left: 10px;
    font-family: "Open Sans", sans-serif;
    font-size: 12px;
    line-height: 1.4;
  }

  /* Lockup */
  .lockup {
    position: absolute;
    left: 40px;
    top: 1100px;
    display: flex;
    align-items: center;
    gap: 16px;
  }
  .lockup .mark-dot {
    width: 46px;
    height: 46px;
    border-radius: 50%;
    background: var(--ink-dark);
  }
  .lockup .brand-name {
    font-family: "Questrial", sans-serif;
    font-size: 56px;
    line-height: 1;
    color: var(--ink-dark);
  }
</style>
</head>
<body>
<main class="canvas">
  <section class="card card-back" aria-label="Card back">
    <span class="mark-dot"></span>
    <span class="brand-name">Lumen Stride</span>
  </section>

  <section class="card card-front" aria-label="Card front">
    <div class="brand-row">
      <span class="mark-dot"></span>
      <span class="brand-name">Lumen Stride</span>
    </div>
    <div class="person">
      <p class="person-name">MARA QUILL</p>
      <p class="person-role">Founder</p>
    </div>
    <div class="contact">
      <span class="mark-dot"></span>
      <div class="contact-lines">
        <p>555.014.2290</p>
        <p>mara@lumenstride-example.net</p>
        <p>www.lumenstride-example.net</p>
      </div>
    </div>
  </section>

  <div class="lockup">
    <span class="mark-dot"></span>
    <span class="brand-name">Lumen Stride</span>
  </div>
</main>
</body>
</html>
```